ulmar stationary etc..
Business Card, Stationary and Envelope Design
Please upload ai or eps of your logo.
The business cards need to be double sided
Hi sir,
I submitted my design please let the feedback and suggestions
Thank you
Veltrusa

```html
<!DOCTYPE html>
<html lang="en">
<head>
<meta charset="utf-8">
<title>ulmar stationery</title>
<link href="https://fonts.googleapis.com/css2?family=Exo+2:wght@400;600;700&family=Tinos&display=swap" rel="stylesheet">
<style>
  :root {
    --bg-dark: #161b21;
    --bg-light: #46525d;
    --blue: #1b78cf;
    --blue-light: #3aa0ea;
    --purple: #3a1e8e;
    --violet: #5a2fb0;
    --paper: #ffffff;
    --ink: #3a3f47;
    --muted: #8a9099;
  }
  * { box-sizing: border-box; margin: 0; padding: 0; }
  html, body { width: 1200px; height: 806px; overflow: hidden; }
  body {
    background: radial-gradient(ellipse at 40% 30%, var(--bg-light), var(--bg-dark) 75%);
    font-family: "Exo 2", sans-serif;
    position: relative;
  }
  .brand { color: var(--blue); font-weight: 700; line-height: 1; letter-spacing: 0.5px; }
  .brand-name { display: block; }
  .brand-tag { display: block; font-weight: 600; color: var(--muted); letter-spacing: 2.5px; }
  .band { position: absolute; left: 0; bottom: 0; width: 100%; }
  .band svg { display: block; width: 100%; height: 100%; }
  .band-url {
    position: absolute; right: 14px; bottom: 8px;
    color: #fff; font-size: 12px; font-weight: 600;
  }
  .address { position: absolute; text-align: right; font-size: 6.5px; color: var(--muted); line-height: 1.5; }

  /* Letterhead */
  .letterhead {
    position: absolute; left: 648px; top: 43px; width: 504px; height: 713px;
    background: var(--paper); box-shadow: 0 6px 24px rgba(0,0,0,.45);
  }
  .letterhead .brand { position: absolute; left: 24px; top: 22px; }
  .letterhead .brand-name { font-size: 34px; }
  .letterhead .brand-tag { font-size: 7px; margin-top: 2px; }
  .letterhead .address { right: 26px; top: 26px; }
  .letter-body {
    position: absolute; left: 34px; top: 140px; width: 420px;
    font-family: "Tinos", serif; font-size: 8.4px; color: var(--ink); line-height: 1.45;
  }
  .letter-body p { margin-bottom: 11px; }
  .letter-body .closing { margin-top: 26px; }
  .letterhead .band { height: 72px; }

  /* Envelope */
  .envelope {
    position: absolute; left: 132px; top: 540px; width: 511px; height: 233px;
    background: var(--paper); box-shadow: 0 6px 24px rgba(0,0,0,.45);
  }
  .envelope .brand { position: absolute; left: 22px; top: 36px; }
  .envelope .brand-name { font-size: 36px; }
  .envelope .brand-tag { font-size: 7px; margin-top: 2px; }
  .envelope .address { right: 24px; top: 40px; }
  .envelope .band { height: 58px; }

  /* Business cards */
  .card {
    position: absolute; top: 345px; width: 230px; height: 135px;
    border-radius: 3px; overflow: hidden; box-shadow: 0 6px 18px rgba(0,0,0,.5);
  }
  .card-front { left: 150px; background: linear-gradient(180deg, #fff, #e9edf2); }
  .card-front .brand { position: absolute; left: 14px; top: 26px; }
  .card-front .brand-name { font-size: 28px; }
  .card-front .brand-tag { font-size: 5.5px; }
  .card-front .swoosh { position: absolute; right: 0; top: 0; width: 120px; height: 135px; }
  .card-front .holder {
    position: absolute; right: 12px; top: 26px; text-align: right; color: #fff;
  }
  .holder-name { font-size: 12px; font-weight: 700; }
  .holder-role { font-size: 6.5px; }
  .holder-contact { font-size: 5.5px; margin-top: 14px; line-height: 1.5; }
  .card-front .band { height: 26px; }
  .card-front .band-url { font-size: 8px; bottom: 6px; right: 10px; }

  .card-back {
    left: 395px;
    background: radial-gradient(ellipse at 50% 40%, var(--blue-light), var(--violet) 55%, var(--purple));
    display: flex; flex-direction: column; align-items: center; justify-content: center;
  }
  .card-back .brand { color: #fff; text-align: center; }
  .card-back .brand-name { font-size: 36px; }
  .card-back .brand-tag { font-size: 6px; color: #d9e6ff; margin-top: 2px; }
  .card-back .holder-first { color: #fff; font-size: 15px; font-weight: 700; margin-top: 14px; }
</style>
</head>
<body>

<svg width="0" height="0" style="position:absolute">
  <defs>
    <linearGradient id="bandFill" x1="0" x2="1" y1="0" y2="0">
      <stop offset="0" stop-color="#3a1e8e"/>
      <stop offset="0.55" stop-color="#4d2aa8"/>
      <stop offset="1" stop-color="#1b78cf"/>
    </linearGradient>
    <linearGradient id="swooshFill" x1="0" x2="1" y1="0" y2="1">
      <stop offset="0" stop-color="#3aa0ea"/>
      <stop offset="1" stop-color="#3a1e8e"/>
    </linearGradient>
  </defs>
</svg>

<!-- Business card: front -->
<section class="card card-front">
  <svg class="swoosh" viewBox="0 0 120 135" preserveAspectRatio="none" aria-hidden="true">
    <path d="M40 0 H120 V135 H0 C50 110 20 40 40 0 Z" fill="url(#swooshFill)"/>
  </svg>
  <div class="brand">
    <span class="brand-name">ulmar</span>
    <span class="brand-tag">CLOUD COMPUTING</span>
  </div>
  <div class="holder">
    <div class="holder-name">John Doe</div>
    <div class="holder-role">Sales Manager</div>
    <div class="holder-contact">Tel 555 010 2040<br>info@ulmar.com</div>
  </div>
  <div class="band">
    <svg viewBox="0 0 230 26" preserveAspectRatio="none" aria-hidden="true">
      <rect width="230" height="26" fill="url(#bandFill)"/>
    </svg>
    <span class="band-url">www.ulmar.com</span>
  </div>
</section>

<!-- Business card: back -->
<section class="card card-back">
  <div class="brand">
    <span class="brand-name">ulmar</span>
    <span class="brand-tag">CLOUD COMPUTING</span>
  </div>
  <div class="holder-first">John</div>
</section>

<!-- Envelope -->
<section class="envelope">
  <div class="brand">
    <span class="brand-name">ulmar</span>
    <span class="brand-tag">CLOUD COMPUTING</span>
  </div>
  <div class="address">123 Cloud Street, Suite 40, Denver, CO 80202<br>Tel 555 010 2040 · info@ulmar.com</div>
  <div class="band">
    <svg viewBox="0 0 511 58" preserveAspectRatio="none" aria-hidden="true">
      <path d="M0 14 C160 28 340 26 511 6 V58 H0 Z" fill="url(#bandFill)"/>
      <path d="M0 10 C160 24 340 22 511 2 V8 C340 28 160 30 0 16 Z" fill="#cfd8e6"/>
    </svg>
    <span class="band-url">www.ulmar.com</span>
  </div>
</section>

<!-- Letterhead -->
<section class="letterhead">
  <div class="brand">
    <span class="brand-name">ulmar</span>
    <span class="brand-tag">CLOUD COMPUTING</span>
  </div>
  <div class="address">123 Cloud Street, Suite 40, Denver, CO 80202<br>Tel 555 010 2040 · info@ulmar.com</div>
  <div class="letter-body">
    <p>Dear Sir or Madam:</p>
    <p>We are pleased to share our latest plans for secure cloud storage and hosting services. Our team will support your move with care and clear guidance at every step.</p>
    <p>Please review the attached outline and let us know which options suit your needs best.</p>
    <p>Our platform offers flexible plans, daily backups and round the clock monitoring for every account. Each service can grow with your business, and our engineers are ready to answer questions at any time. We also provide training sessions for your staff.</p>
    <p>We would welcome the chance to meet with you and discuss how our services can help your organisation reach its goals. Please contact our office to arrange a suitable date, and we will prepare a detailed proposal in advance of the meeting.</p>
    <p class="closing">Yours sincerely</p>
    <p class="closing">John Doe</p>
  </div>
  <div class="band">
    <svg viewBox="0 0 504 72" preserveAspectRatio="none" aria-hidden="true">
      <path d="M0 20 C170 36 340 32 504 8 V72 H0 Z" fill="url(#bandFill)"/>
      <path d="M0 15 C170 31 340 27 504 3 V10 C340 34 170 38 0 22 Z" fill="#cfd8e6"/>
    </svg>
    <span class="band-url">www.ulmar.com</span>
  </div>
</section>

</body>
</html>
```